Ward Compass Business Card Design*

We need a business card design for our company Ward Compass. Our company is specialized in providing online consulting services regarding medical institutions, hospitals and doctors. We work with patients worldwide looking to choose between healthcare providers. We have a website you may use as a reference, where we list doctors and clinics worldwide. So we target Medical providers as well as patients worldwide.
Target Market(s)
Medical Providers and patients around the world
Industry/Entity Type
Medical
Contact Information for Business Card
Salma Derkaoui
CEO
+90 612 348 2071
info@wardcompass-example.com
www.wardcompass-example.com
14 Annakhil 3 H.R.B. Rabat, Morocco
Requirements
Must have
- Company logo/name on one full side, personal info and smaller logo and company name on the other side.
Nice to have
- Smart and elegant design

```html
<!DOCTYPE html>
<html lang="en">
<head>
<meta charset="utf-8">
<title>Ward Compass – Business Card</title>
<link href="https://fonts.googleapis.com/css2?family=Montserrat:wght@500;600;700&family=Lato:wght@400;700&display=swap" rel="stylesheet">
<style>
  :root {
    --navy: #14345f;
    --grey: #6f6f6f;
    --ink: #2b2b2b;
    --text: #4a4a4a;
    --paper: #f7f7f7;
    --paper-shade: #e6e6e6;
    --backdrop: #d9dadc;
  }
  * { margin: 0; padding: 0; box-sizing: border-box; }
  html, body { width: 1200px; height: 900px; overflow: hidden; }
  body {
    background: var(--backdrop);
    display: flex;
    flex-direction: column;
    align-items: center;
    justify-content: center;
    gap: 30px;
  }
  .card {
    width: 700px;
    height: 400px;
    background: linear-gradient(160deg, var(--paper-shade) 0%, var(--paper) 70%);
    border-bottom: 5px solid var(--navy);
    box-shadow: 0 8px 24px rgba(0,0,0,0.18);
    position: relative;
  }
  .wordmark {
    display: flex;
    align-items: center;
    gap: 14px;
    font-family: "Montserrat", sans-serif;
    font-weight: 600;
    color: var(--navy);
    text-transform: uppercase;
    letter-spacing: 0.04em;
    white-space: nowrap;
  }
  .wordmark-dot {
    border-radius: 50%;
    background: var(--navy);
    flex: none;
  }

  /* front */
  .card-front .wordmark {
    position: absolute;
    left: 44px;
    top: 178px;
    font-size: 26px;
  }
  .card-front .wordmark-dot { width: 40px; height: 40px; }
  .divider {
    position: absolute;
    left: 385px;
    top: 70px;
    width: 2px;
    height: 260px;
    background: var(--navy);
  }
  .contact {
    position: absolute;
    left: 412px;
    top: 76px;
    font-family: "Lato", sans-serif;
    color: var(--text);
  }
  .person-name {
    font-family: "Montserrat", sans-serif;
    font-weight: 700;
    font-size: 30px;
    line-height: 1.1;
    color: var(--grey);
  }
  .person-name .first { color: var(--navy); }
  .person-role {
    font-family: "Montserrat", sans-serif;
    font-weight: 700;
    font-size: 17px;
    color: var(--ink);
    margin: 4px 0 14px 10px;
  }
  .address {
    font-size: 17px;
    line-height: 1.35;
    margin-left: 18px;
    margin-bottom: 14px;
  }
  .contact-list { list-style: none; margin-left: 18px; }
  .contact-list li {
    display: flex;
    align-items: center;
    gap: 12px;
    font-size: 17px;
    line-height: 1.75;
  }
  .contact-list svg { width: 18px; height: 18px; flex: none; }

  /* back */
  .card-back { display: flex; align-items: center; justify-content: center; }
  .card-back .wordmark { font-size: 40px; gap: 20px; }
  .card-back .wordmark-dot { width: 58px; height: 58px; }
</style>
</head>
<body>

<section class="card card-front">
  <div class="wordmark"><span class="wordmark-dot"></span>Ward Compass</div>
  <div class="divider"></div>
  <div class="contact">
    <h1 class="person-name"><span class="first">Salma</span> Derkaoui</h1>
    <p class="person-role">CEO</p>
    <p class="address">14 Annakhil 3 H.R.B.<br>Rabat, Morocco</p>
    <ul class="contact-list">
      <li>
        <svg viewBox="0 0 24 24" aria-hidden="true"><path fill="#14345f" d="M6.6 10.8a15.1 15.1 0 0 0 6.6 6.6l2.2-2.2c.3-.3.7-.4 1-.2 1.1.4 2.3.6 3.6.6.6 0 1 .4 1 1V20c0 .6-.4 1-1 1A17 17 0 0 1 3 4c0-.6.4-1 1-1h3.5c.6 0 1 .4 1 1 0 1.3.2 2.5.6 3.6.1.3 0 .7-.2 1z"/></svg>
        +90 612 348 2071
      </li>
      <li>
        <svg viewBox="0 0 24 24" aria-hidden="true"><rect x="2" y="5" width="20" height="14" fill="#14345f"/><path d="M2.5 5.5 12 13l9.5-7.5" fill="none" stroke="#f7f7f7" stroke-width="1.5"/></svg>
        info@wardcompass-example.com
      </li>
      <li>
        <svg viewBox="0 0 24 24" aria-hidden="true"><g fill="none" stroke="#14345f" stroke-width="1.6"><circle cx="12" cy="12" r="9.5"/><ellipse cx="12" cy="12" rx="4.2" ry="9.5"/><path d="M2.5 12h19M4 7h16M4 17h16"/></g></svg>
        www.wardcompass-example.com
      </li>
    </ul>
  </div>
</section>

<section class="card card-back">
  <div class="wordmark"><span class="wordmark-dot"></span>Ward Compass</div>
</section>

</body>
</html>
```